Pelton|Marsh & Quillan business card contest

We need a logo for an upscale boutique diversified company involved in real estate, investments, cattle, and more. Our businesses DO NOT need to be reflected in the business card nor do we want them noted. This is our logo and colors and we love our logo and colors. Our logo looks best against a black background and we like to include the firm name in our logo usage. importantly, the names Pelton and Marsh are separated by | not / and we use an ampersand not the word and.
On the front of the card, we want to include:
company logo and name (Pelton|Marsh & Quillan)
on the back, we would definitely include:
address, email, cell #
logo and name (smaller size than front)

The variable will be location of individual name and title (mine for example is ) - whether on the front OR on the back. interested in variations from which to choose
Dr. Neil R. Whitcombe, CFA
Scientifique des Fusées Financières

we would like to use contemporary symbols for address, email address, cell # with an option for web site that we do not intend to use initially. we like two sided cards and believe this design should use four rounded corners with the standard size. we prefer thicker card stock and may look at metal.

```html
<!DOCTYPE html>
<html lang="en">
<head>
<meta charset="utf-8">
<title>Pelton|Marsh &amp; Quillan — Business Card</title>
<link rel="stylesheet" href="https://fonts.googleapis.com/css2?family=Roboto:wght@400;700&display=swap">
<style>
  :root {
    --orange: #e68124;
    --orange-line: #c9671a;
    --ink: #636363;
    --paper: #ffffff;
    --cream: #fdf1e4;
  }
  * { margin: 0; padding: 0; box-sizing: border-box; }
  html, body { width: 1200px; height: 1200px; overflow: hidden; }
  body {
    background: var(--orange);
    font-family: "Roboto", Arial, sans-serif;
    position: relative;
  }
  .card {
    position: absolute;
    left: 274px;
    width: 709px;
    height: 425px;
    border-radius: 12px;
    overflow: hidden;
    background: var(--paper);
    outline: 1px solid rgba(120, 60, 10, 0.25);
  }
  .card--front { top: 138px; }
  .card--back { top: 658px; }

  .side-tab {
    position: absolute;
    top: 114px;
    width: 21px;
    height: 198px;
    background: var(--orange);
  }
  .side-tab--left { left: 0; }
  .side-tab--right { right: 0; }

  .wordmark {
    position: absolute;
    display: flex;
    align-items: center;
    white-space: nowrap;
    color: var(--ink);
    font-weight: 400;
    transform: translateX(-50%);
  }
  .wordmark__square {
    background: var(--orange);
    flex: none;
  }
  .wordmark--front {
    left: 50%;
    top: 188px;
    font-size: 38px;
    gap: 16px;
  }
  .wordmark--front .wordmark__square { width: 30px; height: 30px; }
  .wordmark--back {
    left: 166px;
    top: 200px;
    font-size: 22px;
    gap: 10px;
  }
  .wordmark--back .wordmark__square { width: 18px; height: 18px; }

  .info-panel {
    position: absolute;
    left: 332px;
    top: 0;
    right: 0;
    bottom: 0;
    background: var(--orange);
  }
  .info-panel__rule {
    position: absolute;
    left: 20px;
    top: 100px;
    width: 2px;
    height: 228px;
    background: var(--orange-line);
  }
  .person {
    position: absolute;
    left: 32px;
    top: 104px;
    color: var(--cream);
  }
  .person__name {
    font-size: 23px;
    font-weight: 700;
    line-height: 1.2;
  }
  .person__title {
    font-size: 17px;
    font-weight: 400;
    margin-top: 2px;
  }
  .contacts {
    position: absolute;
    left: 27px;
    top: 197px;
    list-style: none;
    color: var(--cream);
    font-size: 17.5px;
  }
  .contacts__item {
    display: flex;
    align-items: center;
    gap: 5px;
    height: 31.5px;
  }
  .contacts__icon {
    width: 21px;
    height: 21px;
    flex: none;
  }
</style>
</head>
<body>

  <section class="card card--front" aria-label="Card front">
    <div class="side-tab side-tab--left"></div>
    <div class="side-tab side-tab--right"></div>
    <div class="wordmark wordmark--front">
      <span class="wordmark__square"></span>
      <span class="wordmark__name">Pelton|Marsh &amp; Quillan</span>
    </div>
  </section>

  <section class="card card--back" aria-label="Card back">
    <div class="wordmark wordmark--back">
      <span class="wordmark__square"></span>
      <span class="wordmark__name">Pelton|Marsh &amp; Quillan</span>
    </div>

    <div class="info-panel">
      <div class="info-panel__rule"></div>
      <div class="person">
        <p class="person__name">Dr. Neil R. Whitcombe, CFA</p>
        <p class="person__title">Scientifique Des Fusées Financières</p>
      </div>
      <ul class="contacts">
        <li class="contacts__item">
          <svg class="contacts__icon" viewBox="0 0 24 24" aria-hidden="true">
            <circle cx="12" cy="12" r="12" fill="#fff"/>
            <rect x="8.5" y="5.5" width="7" height="13" rx="1.2" fill="none" stroke="#e68124" stroke-width="1.6"/>
            <circle cx="12" cy="16" r="0.9" fill="#e68124"/>
          </svg>
          <span>555 204 7316</span>
        </li>
        <li class="contacts__item">
          <svg class="contacts__icon" viewBox="0 0 24 24" aria-hidden="true">
            <circle cx="12" cy="12" r="12" fill="#fff"/>
            <rect x="6" y="8" width="12" height="8.5" rx="1" fill="none" stroke="#e68124" stroke-width="1.6"/>
            <path d="M6.5 8.6 L12 13 L17.5 8.6" fill="none" stroke="#e68124" stroke-width="1.6"/>
          </svg>
          <span>hello@pmqoffice.net</span>
        </li>
        <li class="contacts__item">
          <svg class="contacts__icon" viewBox="0 0 24 24" aria-hidden="true">
            <circle cx="12" cy="12" r="12" fill="#fff"/>
            <g fill="none" stroke="#e68124" stroke-width="1.4">
              <circle cx="12" cy="12" r="6.5"/>
              <ellipse cx="12" cy="12" rx="2.8" ry="6.5"/>
              <line x1="5.5" y1="12" x2="18.5" y2="12"/>
              <line x1="6.5" y1="8.8" x2="17.5" y2="8.8"/>
              <line x1="6.5" y1="15.2" x2="17.5" y2="15.2"/>
            </g>
          </svg>
          <span>www.pmqgroup.net</span>
        </li>
        <li class="contacts__item">
          <svg class="contacts__icon" viewBox="0 0 24 24" aria-hidden="true">
            <circle cx="12" cy="12" r="12" fill="#fff"/>
            <path d="M12 19.5 C9 15.5 7.2 12.8 7.2 10.2 A4.8 4.8 0 0 1 16.8 10.2 C16.8 12.8 15 15.5 12 19.5 Z" fill="#e68124"/>
            <circle cx="12" cy="10.2" r="1.8" fill="#fff"/>
          </svg>
          <span>47, Alder Court, Ridge Lane, Country</span>
        </li>
      </ul>
    </div>
  </section>

</body>
</html>
```